Restaurant menu design

I need a menu for a restaurant in Spain.
It has to be bohemian but modern. We need something romantic and elegant.
The restaurant is elegant with good food and an excellent reputation. It is also modern at the same time.
The restaurant is superbly decorated and very chick so we need something "class" to fit in with the surroundings.
The size of the document must be 325 mm in high and 245 mm as a maximum and preferably made in indesign.

Reason: Thank you all for your designs.
So far all your designs are ok but it isn´t what we are looking for. Most of the designs are too loaded, too many colors and too much decoration.

Target Market(s)

Adults of various age groups and different nationalities mostly European.

Industry/Entity Type

Restaurant

Requirements
Must have
• The menu must have two interior pages with the text as in the document attached.It must be easily legible.
Nice to have
• See what kind of menus they use in important restaurants in places like Paris, see what designs are in trend, but Not necessarily doing the same style if it doesn’t fit in with the description above.
Should not have
• Nothing old fashioned.

```html
<!DOCTYPE html>
<html lang="es">
<head>
<meta charset="utf-8">
<title>La Violeta – Carta</title>
<link rel="stylesheet" href="https://fonts.googleapis.com/css2?family=Cormorant+Garamond:ital,wght@0,500;1,400&family=Great+Vibes&display=swap">
<style>
  :root {
    --plum: #2d0915;
    --plum-deep: #250611;
    --paper: #ffffff;
    --ink-light: #f3e9ec;
    --ink-soft: #cdb9bf;
    --accent-red: #d9302c;
    --stripe-grey: #c9c9c9;
    --stripe-black: #0c0c0c;
    --violet: #8a3fb6;
    --fold: rgba(0,0,0,0.45);
  }
  * { box-sizing: border-box; margin: 0; padding: 0; }
  html, body {
    width: 1200px; height: 900px; overflow: hidden;
    background: var(--paper);
  }
  .canvas { position: relative; width: 1200px; height: 900px; }

  /* Cover */
  .cover {
    position: absolute; left: 40px; top: 211px;
    width: 360px; height: 478px;
    background: var(--plum);
    display: flex;
  }
  .cover-field { position: relative; width: 216px; height: 100%; }
  .cover-brand {
    position: absolute; left: 26px; top: 206px;
    display: flex; align-items: center; gap: 10px;
    font-family: "Cormorant Garamond", serif; font-weight: 500;
    font-size: 34px; color: var(--paper); letter-spacing: 0.5px;
    white-space: nowrap;
  }
  .cover-brand .mark {
    width: 14px; height: 14px; border-radius: 50%; background: var(--violet);
  }
  .stripe-grey { width: 10px; background: var(--stripe-grey); }
  .stripe-black { width: 6px; background: var(--stripe-black); }
  .cover-photo {
    flex: 1;
    background: linear-gradient(180deg, #fbf7f8 0%, #efe6ea 40%, #b33a4a 62%, #9e1f2e 100%);
  }

  /* Spread */
  .spread {
    position: absolute; left: 440px; top: 211px;
    width: 720px; height: 478px;
    display: flex;
  }
  .page {
    position: relative; width: 360px; height: 100%;
    background: var(--plum);
    padding: 22px 30px 20px 30px;
    font-family: "Cormorant Garamond", serif; font-style: italic;
    color: var(--ink-light);
    overflow: hidden;
  }
  .page-left { box-shadow: inset -10px 0 14px -10px var(--fold); }
  .page-right { box-shadow: inset 10px 0 14px -10px var(--fold); }

  .section-title {
    font-family: "Great Vibes", cursive; font-weight: 400;
    color: var(--accent-red); font-size: 25px;
    text-align: center; line-height: 1; margin: 6px 0 8px;
  }
  .menu-list { list-style: none; }
  .menu-item {
    display: flex; justify-content: space-between; gap: 12px;
    font-size: 10.5px; line-height: 13.6px;
  }
  .menu-item .price { color: var(--ink-soft); white-space: nowrap; }
  .section + .section { margin-top: 10px; }

  .sauces {
    font-size: 10px; line-height: 13px; margin-top: 7px; color: var(--ink-soft);
  }
  .sauces .label { color: var(--accent-red); }
</style>
</head>
<body>
<main class="canvas">

  <section class="cover">
    <div class="cover-field">
      <div class="cover-brand"><span class="mark"></span>La Violeta</div>
    </div>
    <div class="stripe-grey"></div>
    <div class="stripe-black"></div>
    <div class="cover-photo" role="img" aria-label="Fotografía de dos copas de vino tinto y una botella sobre un mantel rojo"></div>
  </section>

  <section class="spread">
    <article class="page page-left">
      <div class="section">
        <h2 class="section-title">Entradas</h2>
        <ul class="menu-list">
          <li class="menu-item"><span>Ensalada La Violeta, lechuga, tomate</span><span class="price">7,50 €</span></li>
          <li class="menu-item"><span>Ensalada Caprese (Tomate y Mozzarella)</span><span class="price">7,95 €</span></li>
          <li class="menu-item"><span>Escarola al Queso de Cabra con Bacon</span><span class="price">8,25 €</span></li>
          <li class="menu-item"><span>Cóctel de Gambas, Langostinos y Aguacate</span><span class="price">9,90 €</span></li>
          <li class="menu-item"><span>La Sopa de Pescado</span><span class="price">8,25 €</span></li>
          <li class="menu-item"><span>Crema de Espárragos Trigueros y Calabacín</span><span class="price">6,95 €</span></li>
          <li class="menu-item"><span>Carpaccio de Ternera</span><span class="price">9,50 €</span></li>
          <li class="menu-item"><span>Carpaccio de Salmón al Eneldo</span><span class="price">9,50 €</span></li>
          <li class="menu-item"><span>Carpaccio de Atún</span><span class="price">10,50 €</span></li>
          <li class="menu-item"><span>Melón con Jamón Ibérico</span><span class="price">11,50 €</span></li>
          <li class="menu-item"><span>Parrillada de Verduras</span><span class="price">7,95 €</span></li>
          <li class="menu-item"><span>Parrillada de Verduras Gratinada al Queso de Cabra</span><span class="price">9,25 €</span></li>
          <li class="menu-item"><span>Gambas Rojas de la Bahía</span><span class="price">14,50 €</span></li>
        </ul>
      </div>
      <div class="section">
        <h2 class="section-title">Pescados al Grill</h2>
        <ul class="menu-list">
          <li class="menu-item"><span>Lubina al Horno</span><span class="price">15,90 €</span></li>
          <li class="menu-item"><span>Lubina Rebozada y su Salsa Tártara con Berenjenas</span><span class="price">16,50 €</span></li>
          <li class="menu-item"><span>Filete de Bacalao y su Salsa de Mariscos</span><span class="price">15,25 €</span></li>
          <li class="menu-item"><span>Dorada del Mediterráneo</span><span class="price">15,50 €</span></li>
          <li class="menu-item"><span>Langostinos al Grill con Hierbas Provenzales</span><span class="price">18,75 €</span></li>
          <li class="menu-item"><span>Pez Espada Fresco y su Salsa Ginger</span><span class="price">16,95 €</span></li>
          <li class="menu-item"><span>Lomo de Salmón con Salsa de Frambuesa</span><span class="price">15,95 €</span></li>
          <li class="menu-item"><span>Parrillada de Pescado y Marisco</span><span class="price">24,50 €</span></li>
        </ul>
      </div>
      <div class="section">
        <h2 class="section-title">Especial Niños</h2>
        <ul class="menu-list">
          <li class="menu-item"><span>Solomillo de pollo, huevo y patatas fritas</span><span class="price">8,25 €</span></li>
          <li class="menu-item"><span>Pasta al gusto</span><span class="price">6,95 €</span></li>
        </ul>
      </div>
    </article>

    <article class="page page-right">
      <div class="section">
        <h2 class="section-title">Carnes</h2>
        <ul class="menu-list">
          <li class="menu-item"><span>Pechuga de Pollo "Santa Rosa" con Champiñones y Bacon</span><span class="price">13,95 €</span></li>
          <li class="menu-item"><span>Chuletas de Cordero</span><span class="price">16,50 €</span></li>
          <li class="menu-item"><span>Costillas de Cerdo con Salsa Barbacoa</span><span class="price">14,50 €</span></li>
          <li class="menu-item"><span>Solomillo de Cochinillo Lechal</span><span class="price">18,75 €</span></li>
          <li class="menu-item"><span>La Stroganoff, Finas tiras de Solomillo con su Salsa de Champiñones</span><span class="price">17,50 €</span></li>
          <li class="menu-item"><span>Solomillo de Ternera</span><span class="price">21,50 €</span></li>
          <li class="menu-item"><span>Solomillo de Ternera a la Pimienta verde</span><span class="price">22,75 €</span></li>
          <li class="menu-item"><span>Hamburguesa de Ternera con Huevo y Patatas Fritas</span><span class="price">12,50 €</span></li>
          <li class="menu-item"><span>Solomillo de Cerdo al Horno con Jamón y su Salsa de Setas</span><span class="price">16,95 €</span></li>
          <li class="menu-item"><span>Entrecot de Ternera</span><span class="price">19,50 €</span></li>
          <li class="menu-item"><span>T-Bone Steak de Ternera</span><span class="price">23,95 €</span></li>
          <li class="menu-item"><span>Chuletón de Ternera</span><span class="price">25,50 €</span></li>
          <li class="menu-item"><span>Parrillada de Carnes y Embutidos</span><span class="price">22,95 €</span></li>
        </ul>
        <p class="sauces"><span class="label">Salsas</span> · Pimienta 3,50 € · Roquefort 3,50 € · Mostaza 3,50 € · de Champiñones 3,50 €</p>
      </div>
      <div class="section">
        <h2 class="section-title">Los Postres de la Violeta</h2>
        <ul class="menu-list">
          <li class="menu-item"><span>Profiteroles "La Violeta"</span><span class="price">6,25 €</span></li>
          <li class="menu-item"><span>Cóctel de Frutas Exóticas</span><span class="price">6,95 €</span></li>
          <li class="menu-item"><span>Sorbete de Limón, Cava y Vodka</span><span class="price">5,95 €</span></li>
          <li class="menu-item"><span>Fondant de Chocolate Caliente con su Salsa de Vainilla</span><span class="price">6,50 €</span></li>
          <li class="menu-item"><span>Crème Brûlée</span><span class="price">5,95 €</span></li>
          <li class="menu-item"><span>Tarta de Manzana Caliente y su Helado de Tomillo</span><span class="price">6,50 €</span></li>
          <li class="menu-item"><span>Copa Glaciar Dorado</span><span class="price">5,50 €</span></li>
          <li class="menu-item"><span>Pera al Chocolate Caliente y Helado de Macadamia</span><span class="price">6,75 €</span></li>
          <li class="menu-item"><span>Tarta de Queso con Coulis de Fresa</span><span class="price">5,95 €</span></li>
          <li class="menu-item"><span>Surtido Mousse de Chocolate</span><span class="price">5,75 €</span></li>
        </ul>
      </div>
    </article>
  </section>

</main>
</body>
</html>
```